Brochure for a software solution

Dear all,
PLEASE DO NOT SUBMIT YOUR DESIGNS IF YOU WERE NOT INVITED.
This was meant to be setup as a job for one designer only.
Apologies for the confusion.
Thank you.
Dear all,
This was meant to be setup as a job or one designer only.
Thank you.
Software

```html
<!DOCTYPE html>
<html lang="en">
<head>
<meta charset="utf-8">
<title>Lumen Insight Brochure Cover</title>
<link rel="stylesheet" href="https://fonts.googleapis.com/css2?family=Ubuntu:wght@400;500;700&display=swap">
<style>
  :root {
    --stage: #1a1a1a;
    --paper: #ffffff;
    --rule-grey: #dedede;
    --sun-light: #ffe45a;
    --sun-mid: #ffcf1f;
    --sun-deep: #f8aa1c;
    --sun-edge: #f08c12;
    --band-edge: #ffc400;
    --ink-dark: #2b2418;
    --ink-light: #fffbe8;
  }
  * { margin: 0; padding: 0; box-sizing: border-box; }
  html, body {
    width: 1200px; height: 824px; overflow: hidden;
    background: var(--stage);
    font-family: "Ubuntu", sans-serif;
  }
  .cover {
    position: absolute; left: 150px; top: 92px;
    width: 900px; height: 640px;
    background: var(--paper);
    display: flex; flex-direction: column;
  }
  .band-white-top { height: 48px; background: var(--paper); }
  .band-grey { height: 14px; background: var(--rule-grey); }
  .sun-panel {
    position: relative; flex: 1; overflow: hidden;
    border-bottom: 6px solid var(--band-edge);
  }
  .sun-backdrop {
    position: absolute; inset: 0;
    background: linear-gradient(160deg, var(--sun-light) 0%, var(--sun-mid) 40%, var(--sun-deep) 78%, var(--sun-edge) 100%);
  }
  .brand {
    position: absolute; right: 110px; top: 58px;
    display: flex; align-items: center; gap: 10px;
  }
  .brand-dot { width: 38px; height: 38px; border-radius: 50%; background: var(--ink-dark); }
  .brand-name { font-size: 30px; font-weight: 700; color: var(--ink-dark); letter-spacing: .5px; }
  .headline {
    position: absolute; right: 70px; top: 190px; text-align: right;
    color: var(--ink-dark);
  }
  .headline h1 { font-size: 28px; font-weight: 400; letter-spacing: .3px; }
  .headline p { font-size: 12px; color: var(--ink-light); margin-top: 4px; letter-spacing: .6px; }
  .product-row {
    position: absolute; right: 70px; top: 268px;
    display: flex; align-items: center; gap: 22px;
    color: var(--ink-light);
  }
  .product-row .placeholder { font-size: 10px; letter-spacing: 1px; margin-right: 40px; }
  .divider { width: 1px; height: 42px; background: rgba(255,255,255,.6); }
  .product { display: flex; align-items: center; gap: 8px; font-size: 16px; font-weight: 700; }
  .product .circle { width: 20px; height: 20px; border-radius: 50%; border: 2px solid var(--ink-light); }
  .product .square { width: 18px; height: 18px; background: var(--ink-light); }
  .band-white-bottom { height: 78px; background: var(--paper); }
</style>
</head>
<body>
  <main class="cover">
    <div class="band-white-top"></div>
    <div class="band-grey"></div>
    <section class="sun-panel">
      <div class="sun-backdrop" role="img" aria-label="Warm yellow-orange backdrop with sunburst glow and flowing light lines"></div>
      <div class="brand">
        <span class="brand-dot"></span>
        <span class="brand-name">LUMEN INSIGHT</span>
      </div>
      <div class="headline">
        <h1>Making Information Available</h1>
        <p>Providing actionable business intelligence information</p>
      </div>
      <div class="product-row">
        <span class="placeholder">LOGO</span>
        <span class="divider"></span>
        <span class="product"><span class="circle"></span>LUMEN SEARCH</span>
        <span class="divider"></span>
        <span class="product"><span class="square"></span>LUMEN ANALYTICS</span>
      </div>
    </section>
    <div class="band-grey"></div>
    <div class="band-white-bottom"></div>
  </main>
</body>
</html>
```